Innovative psychologist for companies seeks web design for website

Psychologist offers 2 topics:
1. What can a company do to ensure that employees are satisfied and enjoy their work?
The following explanatory video is linked on the website:
https://www.vidplumora.com/watch?v=qTr8ZpLmW3d
2. How can you successfully change your own behavior?
Explanatory video: https://www.vidplumora.com/watch?v=HxK2vQeRt7b&t=6s
The slogan for the second theme will be: YOU are the pirate of your life!

Target Market(s)

companies and private individuals

Number of Pages Required

1 page

Requirements
Nice to have
• Characteristics of the psychologist: pragmatic, down-to-earth, honest, direct, appreciative, enjoys life, loves nature

```html
<!DOCTYPE html>
<html lang="en">
<head>
<meta charset="utf-8">
<title>Jonas Wellbrand – Psychologist for Companies</title>
<link rel="stylesheet" href="https://fonts.googleapis.com/css2?family=Poppins:wght@400;500;600;700;800&display=swap">
<style>
  :root {
    --gold: #c5a56a;
    --ink: #111111;
    --muted: #444444;
    --paper: #ffffff;
    --frame: #0a0a0a;
    --photo-warm-1: #f1e6d2;
    --photo-warm-2: #b89c74;
    --photo-warm-3: #5b5146;
    --portrait-1: #efe6dc;
    --portrait-2: #ffffff;
  }
  * { box-sizing: border-box; margin: 0; padding: 0; }
  html, body { width: 915px; height: 1200px; overflow: hidden; background: var(--paper); }
  body { font-family: "Poppins", sans-serif; color: var(--ink); }
  .page { position: relative; width: 915px; height: 1200px; }

  .brand-name {
    position: absolute; left: 58px; top: 18px;
    font-size: 26px; font-weight: 600; color: var(--gold); letter-spacing: 0.2px;
  }
  .header-contact {
    position: absolute; right: 60px; top: 21px;
    font-size: 12px; font-weight: 400; white-space: nowrap;
  }
  .header-contact span + span { margin-left: 12px; }

  .hero {
    position: absolute; left: 41px; top: 64px; width: 832px; height: 464px;
    border-radius: 19px; overflow: hidden;
    background:
      radial-gradient(ellipse at 75% 35%, var(--photo-warm-1) 0%, rgba(241,230,210,0) 55%),
      linear-gradient(135deg, #8a8074 0%, var(--photo-warm-2) 45%, #e9dcc4 70%, var(--photo-warm-3) 100%);
  }
  .hero-headline {
    position: absolute; left: 34px; top: 186px;
    font-size: 29px; font-weight: 800; line-height: 32px; color: var(--paper);
    text-shadow: 0 1px 3px rgba(0,0,0,0.35); white-space: nowrap;
  }

  .intro-quote {
    position: absolute; left: 102px; top: 537px;
    font-size: 20px; line-height: 22px; font-weight: 400; white-space: nowrap;
  }

  .topics {
    position: absolute; left: 102px; top: 662px; width: 720px;
    font-size: 11px; line-height: 16px; color: var(--muted);
  }
  .topics strong { color: var(--ink); font-weight: 600; }
  .topics .slogan { color: var(--gold); font-weight: 600; }
  .topics a { color: var(--muted); text-decoration: underline; }

  .portrait {
    position: absolute; left: 555px; top: 714px; width: 282px; height: 303px;
    background: radial-gradient(ellipse at 52% 55%, var(--portrait-1) 0%, var(--portrait-1) 35%, var(--portrait-2) 75%);
  }
  .about-card {
    position: absolute; left: 68px; top: 745px; width: 771px; height: 391px;
    border: 4px solid var(--frame); border-radius: 19px;
  }
  .about-text {
    position: absolute; left: 98px; top: 775px;
    font-size: 12.5px; line-height: 18.8px; white-space: nowrap;
  }
  .about-text p + p { margin-top: 18.8px; }
  .cta-line {
    position: absolute; left: 98px; top: 1022px;
    font-size: 13px; white-space: nowrap;
  }
  .cta-line strong { font-size: 14px; font-weight: 600; }
  .card-name {
    position: absolute; left: 621px; top: 1019px;
    font-size: 19px; font-weight: 700; letter-spacing: 0.2px;
  }
  .contact-icon { position: absolute; }
  .icon-phone { left: 125px; top: 1067px; }
  .icon-mail { left: 486px; top: 1071px; }
  .contact-value { position: absolute; font-weight: 400; white-space: nowrap; }
  .phone-value { left: 198px; top: 1075px; font-size: 23px; }
  .mail-value { left: 567px; top: 1075px; font-size: 20.5px; }
</style>
</head>
<body>
<div class="page">
  <div class="brand-name">Jonas Wellbrand</div>
  <div class="header-contact"><span>Email : Jonas.W@mailvista.com</span><span>Phone : +49222000333444</span></div>

  <div class="hero" role="img" aria-label="Photo of a smiling man at an office desk reading a book, with monitors and a desk lamp in warm light">
    <h1 class="hero-headline">Is your employees are satisfied<br>and enjoy their work?</h1>
  </div>

  <p class="intro-quote">“I believe that employees generally come to work with every best<br>intention. After all, they chose their profession and the company they<br>work for Every human wants to do something meaningful and feel<br>satisfied at the end of the day. However, increasing levels of demand<br>and complexity mean that reality can be a different story”.</p>

  <div class="topics">
    <p><strong>1. Satisfied employees who enjoy their work</strong> – explanatory video: <a href="https://www.vidplumora.com/watch?v=qTr8ZpLmW3d">https://www.vidplumora.com/watch?v=qTr8ZpLmW3d</a></p>
    <p><strong>2. How can you successfully change your own behavior?</strong> <span class="slogan">YOU are the pirate of your life!</span></p>
    <p>Explanatory video: <a href="https://www.vidplumora.com/watch?v=HxK2vQeRt7b&amp;t=6s">https://www.vidplumora.com/watch?v=HxK2vQeRt7b&amp;t=6s</a></p>
  </div>

  <div class="portrait" role="img" aria-label="Portrait photo of the psychologist in a white polo shirt"></div>
  <div class="about-card"></div>

  <div class="about-text">
    <p>I have worked for over 20 years as a psychologist and<br>for a number of different companies.<br>I know what options you have to make a change. Corporate culture,<br>leadership, and communication<br>all have a tremendous impact on employee motivation,<br>trust, and performance.<br>I will conduct individual coaching sessions for managers who want to<br>understand their personal behaviour and that of their employees<br>better and want to develop their competences in employee leadership</p>
    <p>So, let's explore together what you can do to bring<br>about the change you want.</p>
  </div>

  <p class="cta-line"><strong>Just call me or send me an email</strong> to take the first step</p>
  <div class="card-name">JONAS WELLBRAND</div>

  <svg class="contact-icon icon-phone" width="54" height="52" viewBox="0 0 54 52" fill="none" stroke="#111" stroke-width="2.4" stroke-linejoin="round" stroke-linecap="round" aria-hidden="true">
    <path d="M8 12 L14 9 L20 19 L15 23 C17 30 22 35 29 38 L33 33 L43 39 L40 45 C36 49 28 48 20 41 C12 34 4 24 8 12 Z"/>
    <rect x="26" y="1.5" width="25" height="17" rx="3"/>
    <path d="M31 18.5 L29 24 L36 18.5"/>
    <circle cx="33" cy="10" r="0.8" fill="#111"/>
    <circle cx="38.5" cy="10" r="0.8" fill="#111"/>
    <circle cx="44" cy="10" r="0.8" fill="#111"/>
  </svg>
  <div class="contact-value phone-value">+49222000333444</div>

  <svg class="contact-icon icon-mail" width="55" height="45" viewBox="0 0 55 45" fill="none" stroke="#111" stroke-width="4" stroke-linejoin="round" stroke-linecap="round" aria-hidden="true">
    <rect x="2.5" y="2.5" width="50" height="40" rx="5"/>
    <path d="M8 10 L27.5 25 L47 10"/>
  </svg>
  <div class="contact-value mail-value">Jonas.W@mailvista.com</div>
</div>
</body>
</html>
```